Web interface for PC desktop app

We need an HTML design for our new PC software.

To get an idea of the project scope, please review the interface draft in the attached files. The screenshot shows almost all dialogs of our product.

Our product is software that allows users to replace static System wallpaper with live animated scenes. The program interface consists of a gallery where users can select and download animated scenes, as well as an information area with scene details and current desktop settings. The product will be distributed on the Vorlo platform among the gamer community.

For this project, you need to create an engaging and user-friendly interface using HTML and CSS in two color schemes (black and white). Additionally, you will need to create a colorized version of the main program icon in vector format (a draft of the program icon is attached), design all other program icons, including icons for the title bar, and redraw all other images according to your design style.

Project Requirements:
-Develop a comprehensive design for the application, including icons and images, in two color schemes: dark and light.
-Colorize our main program icon according to your design style.
-Create other UI icons in all sizes from 16x16 to 512x512 pixels, ensuring that other images are suitable for up to 4K monitors.
-Ensure all UI controls have styles for standard System states: normal, hovered, active, and disabled.

Deliverables:
-Final design in HTML and CSS format.
-Icons in ICO format.
-Images in PNG format.

• all interface elements, including the program title bar, coded in HTML and CSS.

```html
<!DOCTYPE html>
<html lang="en">
<head>
<meta charset="utf-8">
<title>LumaDesk – app interface, light and dark</title>
<link rel="stylesheet" href="https://fonts.googleapis.com/css2?family=Noto+Sans:wght@400;500;600;700&display=swap">
<style>
:root{
  --brand:#1a9be8;
  --stage-dark:#05050c;
  --stage-light:#ffffff;
  --gold:#f6c21b;
  --heart:#e8283a;
}
.light{
  --bar:#efefef;--side:#ffffff;--main:#f6f6f6;--text:#1e1e1e;--muted:#6b6b6b;
  --chip:#eeeeee;--chip-active:#e4e4e4;--field:#ffffff;--line:#e2e2e2;--dim:#a8a8a8;
  --mon:#e8e8e8;--fav-bg:rgba(255,255,255,.55);--fav-icon:#d8d8d8;
  --cta-bg:#111111;--cta-text:#ffffff;--scroll:#cfcfcf;
}
.dark{
  --bar:#0d0d0d;--side:#1b1b1b;--main:#151515;--text:#f1f1f1;--muted:#8a8a8a;
  --chip:#050505;--chip-active:#050505;--field:#050505;--line:#2c2c2c;--dim:#5a5a5a;
  --mon:#2e2e2e;--fav-bg:#050505;--fav-icon:#ffffff;
  --cta-bg:#ffffff;--cta-text:#111111;--scroll:#3a3a3a;
}
*{box-sizing:border-box;margin:0;padding:0}
html,body{width:814px;height:1200px;overflow:hidden;background:var(--stage-light)}
body{font-family:"Noto Sans",Arial,sans-serif}
.stage{position:absolute;left:0;top:0;width:1576px;height:2324px;transform:scale(.5165);transform-origin:0 0;background:var(--stage-light)}
.band{position:absolute;left:0;top:0;width:1576px;height:1237px;background:var(--stage-dark)}
.wordmark{position:absolute;top:80px;display:flex;align-items:center;gap:16px;font-size:36px;font-weight:500;letter-spacing:.2px}
.wordmark .mark{width:63px;height:63px;border-radius:10px;background:var(--brand)}
.wordmark.on-blue{left:147px;color:var(--brand)}
.wordmark.on-white{left:1097px;color:#ffffff}

.window{position:absolute;left:149px;width:1278px;height:835px;overflow:hidden;background:var(--main);color:var(--text)}
.window.light{top:272px}
.window.dark{top:1365px}
svg{display:block}
.ico{width:16px;height:16px;fill:none;stroke:currentColor;stroke-width:1.6;stroke-linecap:round;stroke-linejoin:round}

.titlebar{position:relative;height:57px;background:var(--bar)}
.app-name{position:absolute;left:27px;top:14px;display:flex;align-items:center;gap:8px;color:var(--brand);font-size:17px;font-weight:500}
.app-name .mark{width:29px;height:29px;border-radius:5px;background:var(--brand)}
.win-controls{position:absolute;right:38px;top:17px;display:flex;gap:12px;color:var(--text)}
.win-controls .ico{width:17px;height:17px}

.sidebar{position:absolute;left:0;top:57px;width:356px;bottom:0;background:var(--side)}
.tabs{position:absolute;left:41px;top:28px;display:flex;align-items:center;font-size:17px}
.tabs .tab{display:flex;align-items:center;gap:9px}
.tabs .tab.off{color:var(--dim)}
.tabs .sep{width:1px;height:24px;background:var(--line);margin:0 20px}
.monitor{position:absolute;top:78px;height:100px;display:flex;align-items:center;justify-content:center}
.monitor.current{left:27px;width:147px;background:var(--mon)}
.monitor.second{left:195px;width:118px}
.laptop{display:flex;flex-direction:column;align-items:center}
.laptop .screen{width:108px;height:66px;border:3px solid #1d1d1f;border-radius:4px}
.laptop .base{width:124px;height:3px;background:#8d8d8d;border-radius:0 0 3px 3px}
.second .laptop .screen{width:95px;height:62px}
.second .laptop .base{width:116px}
.info-line{position:absolute;left:27px;font-size:12.5px;color:var(--text)}
.info-line span{color:var(--muted);margin-right:4px}
.row-buttons{position:absolute;left:27px;display:flex;gap:10px;align-items:center}
.btn{height:28px;padding:0 11px;display:flex;align-items:center;gap:6px;background:var(--chip);color:var(--text);font-size:13px;border-radius:3px}
.btn .ico{width:14px;height:14px}
.dots{width:27px;height:27px;border-radius:50%;background:var(--chip);display:flex;align-items:center;justify-content:center;margin-left:2px}
.dots i{display:block;width:3px;height:3px;border-radius:50%;background:var(--text);box-shadow:0 -5px 0 var(--text),0 5px 0 var(--text)}
.divider{position:absolute;left:0;width:356px;height:1px;background:var(--line)}
.preview{position:absolute;left:27px;top:358px;width:301px;height:191px}
.preview .fav{background:#ffffff;width:28px;height:28px;right:10px;top:17px}
.preview .fav svg{fill:var(--heart)}
.preview-title{position:absolute;left:27px;top:577px;font-size:15px;font-weight:700}
.preview-by{position:absolute;left:27px;top:600px;font-size:12.5px;color:var(--muted)}
.preview-spec{position:absolute;left:207px;top:577px;font-size:12.5px;line-height:20px}
.preview-spec span{display:inline-block;width:72px;color:var(--muted)}
.cta{position:absolute;left:27px;top:711px;width:211px;height:31px;background:var(--cta-bg);color:var(--cta-text);font-size:13px;display:flex;align-items:center;gap:7px;padding-left:13px;border-radius:2px}
.cta .ico{width:14px;height:14px}

.content{position:absolute;left:356px;top:57px;right:0;bottom:0}
.source{position:absolute;left:38px;top:23px;display:flex;gap:8px;font-size:13px}
.source .item{height:28px;padding:0 11px 0 4px;display:flex;align-items:center;gap:5px}
.source .item.off{color:var(--dim)}
.light .source .item.off{color:var(--dim)}
.dark .source .item.off{color:var(--text)}
.source .item.on{background:var(--chip-active);padding:0 11px}
.scheme{position:absolute;right:40px;top:21px;display:flex;gap:14px;font-size:13px}
.scheme .item{height:32px;padding:0 12px;display:flex;align-items:center;gap:7px;color:var(--dim)}
.scheme .item.on{background:var(--chip-active);color:var(--text)}
.scheme .item.on.moon{background:#050505}
.scheme .ico{width:18px;height:18px}
.filters{position:absolute;left:30px;top:87px;display:flex;gap:19px;align-items:center}
.field{height:44px;background:var(--field);display:flex;align-items:center;gap:12px;padding:0 22px;font-size:13.5px;color:var(--text)}
.field .ico{width:18px;height:18px;color:var(--muted)}
.dark .field .ico{color:var(--text)}
.field.search{width:282px}
.field.creator{width:120px}
.field.category{width:129px}
.field.rating{width:113px}
.filters .round{width:42px;height:42px;border-radius:50%;background:var(--field);display:flex;align-items:center;justify-content:center}
.filters .round i{display:block;width:3px;height:3px;border-radius:50%;background:var(--muted);box-shadow:0 -5px 0 var(--muted),0 5px 0 var(--muted)}
.dark .filters .round i{background:#fff;box-shadow:0 -5px 0 #fff,0 5px 0 #fff}
.gallery{position:absolute;left:30px;top:165px;display:grid;grid-template-columns:repeat(3,276px);column-gap:18px;row-gap:0}
.card{height:250px}
.thumb{position:relative;width:276px;height:165px}
.stars{position:absolute;left:11px;top:6px;font-size:17px;letter-spacing:1px;color:#ffffff}
.stars b{color:var(--gold);font-weight:400}
.fav{position:absolute;right:13px;top:13px;width:27px;height:27px;border-radius:50%;background:var(--fav-bg);display:flex;align-items:center;justify-content:center}
.fav svg{width:15px;height:15px;fill:var(--fav-icon)}
.meta{display:flex;justify-content:space-between;padding-top:12px}
.meta h3{font-size:15px;font-weight:700;line-height:20px}
.meta p{font-size:12.5px;color:var(--muted);margin-top:2px}
.meta .spec{font-size:12.5px;text-align:right;line-height:20px}
.scrollbar{position:absolute;left:911px;top:165px;width:4px;height:101px;border-radius:2px;background:var(--scroll)}

.art-lake{background:linear-gradient(180deg,#e9889e 0%,#a17ba8 35%,#5f7fae 60%,#2b4b7c 100%)}
.art-sunset{background:linear-gradient(180deg,#2e2752 0%,#a14a5a 35%,#ef6d35 62%,#1a0f10 100%)}
.art-moon{background:radial-gradient(circle at 70% 30%,#b9e4f2 0%,#3c9cc6 35%,#0e3452 100%)}
.art-storm{background:linear-gradient(135deg,#7a7a70 0%,#4a4b45 50%,#1f201d 100%)}
.art-cliff{background:linear-gradient(120deg,#232636 0%,#6a2a26 45%,#d2562d 75%,#f2a263 100%)}
.art-blaze{background:radial-gradient(circle at 45% 55%,#f6d08a 0%,#dc7a34 40%,#8f2c16 100%)}
.art-stars{background:linear-gradient(160deg,#1b2236 0%,#6a3a3a 50%,#dc6e36 100%)}
.art-temple{background:linear-gradient(180deg,#a8986e 0%,#6e6248 55%,#2f2a20 100%)}
.art-neon{background:linear-gradient(90deg,#131c6a 0%,#d01e45 35%,#2a2f9a 60%,#e0283f 85%,#121a5c 100%)}
.art-tree{background:linear-gradient(180deg,#8fc2e0 0%,#e47a5a 45%,#35647e 100%)}
.art-night{background:radial-gradient(circle at 55% 40%,#d8f0f4 0%,#46b1d0 40%,#123e66 100%)}
</style>
</head>
<body>
<div class="stage">
  <div class="band"></div>
  <div class="wordmark on-blue"><span class="mark"></span>LumaDesk</div>
  <div class="wordmark on-white"><span class="mark"></span>LumaDesk</div>

  <!-- LIGHT SCHEME -->
  <section class="window light">
    <header class="titlebar">
      <div class="app-name"><span class="mark"></span>LumaDesk</div>
      <div class="win-controls">
        <svg class="ico" viewBox="0 0 16 16"><path d="M3 8h10"/></svg>
        <svg class="ico" viewBox="0 0 16 16"><rect x="2.5" y="5" width="8.5" height="8.5"/><path d="M5 5V2.5h8.5V11H11"/></svg>
        <svg class="ico" viewBox="0 0 16 16"><path d="M3 3l10 10M13 3L3 13"/></svg>
      </div>
    </header>
    <aside class="sidebar">
      <nav class="tabs">
        <div class="tab"><svg class="ico" viewBox="0 0 16 16"><rect x="2" y="2" width="12" height="12"/><path d="M4 12l3-3 2 2 3-3"/></svg>Wallpapers</div>
        <span class="sep"></span>
        <div class="tab off"><svg class="ico" viewBox="0 0 16 16"><rect x="1.5" y="3" width="13" height="8.5"/><path d="M6 14h4"/></svg>ScreenSavers</div>
      </nav>
      <div class="monitor current"><div class="laptop"><div class="screen art-tree" role="img" aria-label="Tree at dusk wallpaper on first display"></div><div class="base"></div></div></div>
      <div class="monitor second"><div class="laptop"><div class="screen art-night" role="img" aria-label="Moonlit scene wallpaper on second display"></div><div class="base"></div></div></div>
      <p class="info-line" style="top:201px"><span>Display 1:</span>Norvia G13L</p>
      <p class="info-line" style="top:227px"><span>Wallpaper:</span> System Default</p>
      <div class="row-buttons" style="top:263px">
        <div class="btn"><svg class="ico" viewBox="0 0 16 16"><circle cx="8" cy="8" r="2.2"/><path d="M8 1.5v2M8 12.5v2M1.5 8h2M12.5 8h2M3.4 3.4l1.4 1.4M11.2 11.2l1.4 1.4M3.4 12.6l1.4-1.4M11.2 4.8l1.4-1.4"/></svg>Settings</div>
        <div class="btn"><svg class="ico" viewBox="0 0 16 16"><rect x="1.5" y="2.5" width="13" height="9"/><path d="M6 14h4M9 7h4"/></svg>Next</div>
        <div class="btn"><svg class="ico" viewBox="0 0 16 16"><rect x="1.5" y="3.5" width="13" height="9"/><path d="M1.5 6h13"/></svg>View</div>
        <div class="dots"><i></i></div>
      </div>
      <div class="divider" style="top:328px"></div>
      <div class="preview thumb art-lake" role="img" aria-label="Pagoda on a lake at pink sunset">
        <span class="stars"><b>★★★★</b>★</span>
        <span class="fav"><svg viewBox="0 0 16 16"><path d="M8 14S1.5 10 1.5 5.6A3.3 3.3 0 0 1 8 4.2a3.3 3.3 0 0 1 6.5 1.4C14.5 10 8 14 8 14z"/></svg></span>
      </div>
      <h2 class="preview-title">Japan digital art</h2>
      <p class="preview-by">by: LumaDesk</p>
      <p class="preview-spec"><span>Image Size:</span>5.4Mb<br><span>Resolution:</span>3480x2300</p>
      <div class="row-buttons" style="top:626px">
        <div class="btn"><svg class="ico" viewBox="0 0 16 16"><path d="M3 8.5l3 3 7-7"/></svg>Apply</div>
        <div class="btn"><svg class="ico" viewBox="0 0 16 16"><rect x="2" y="3" width="12" height="10"/><path d="M2 6.5h12M2 9.5h12"/></svg>Try</div>
        <div class="btn"><svg class="ico" viewBox="0 0 16 16"><rect x="2" y="2" width="12" height="12"/><path d="M5 8h6"/></svg>Uninstall</div>
        <div class="dots"><i></i></div>
      </div>
      <div class="divider" style="top:682px"></div>
      <div class="cta"><svg class="ico" viewBox="0 0 16 16"><path d="M9 2H2v12h12V7M11 1v5M8.5 3.5h5"/></svg>Create your own Wallpaper</div>
    </aside>
    <main class="content">
      <div class="source">
        <div class="item off"><svg class="ico" viewBox="0 0 16 16"><rect x="2" y="2" width="12" height="12"/><path d="M8 4.5v6M5.5 8l2.5 2.5L10.5 8"/></svg>Installed</div>
        <div class="item on"><svg class="ico" viewBox="0 0 16 16"><rect x="1.5" y="2.5" width="13" height="9"/><path d="M6 14h4"/></svg>Workshop</div>
      </div>
      <div class="scheme">
        <div class="item on"><svg class="ico" viewBox="0 0 16 16"><circle cx="8" cy="8" r="3"/><path d="M8 1v1.8M8 13.2V15M1 8h1.8M13.2 8H15M3 3l1.3 1.3M11.7 11.7L13 13M3 13l1.3-1.3M11.7 4.3L13 3"/></svg>Light</div>
        <div class="item"><svg class="ico" viewBox="0 0 16 16" style="fill:currentColor;stroke:none"><path d="M9.5 1.5a6.5 6.5 0 1 0 5 9.5A5.5 5.5 0 0 1 9.5 1.5z"/></svg>Dark</div>
      </div>
      <div class="filters">
        <div class="field search"><svg class="ico" viewBox="0 0 16 16"><circle cx="7" cy="7" r="5"/><path d="M11 11l3.5 3.5"/></svg>Search for Wallpapers</div>
        <div class="field creator"><svg class="ico" viewBox="0 0 16 16"><circle cx="8" cy="5" r="3"/><path d="M2.5 14.5c0-3 2.5-4.5 5.5-4.5s5.5 1.5 5.5 4.5z"/></svg>Creator</div>
        <div class="field category"><svg class="ico" viewBox="0 0 16 16"><rect x="2" y="2" width="4.5" height="4.5"/><rect x="9.5" y="2" width="4.5" height="4.5"/><rect x="2" y="9.5" width="4.5" height="4.5"/><rect x="9.5" y="9.5" width="4.5" height="4.5"/></svg>Category</div>
        <div class="field rating"><svg class="ico" viewBox="0 0 16 16"><path d="M8 1.8l1.9 3.9 4.3.6-3.1 3 .7 4.3L8 11.6l-3.8 2 .7-4.3-3.1-3 4.3-.6z"/></svg>Rating</div>
        <div class="round"><i></i></div>
      </div>
      <div class="gallery">
        <article class="card"><div class="thumb art-lake" role="img" aria-label="Pagoda on a lake at pink sunset"><span class="stars"><b>★★★★</b>★</span><span class="fav"><svg viewBox="0 0 16 16"><path d="M8 14S1.5 10 1.5 5.6A3.3 3.3 0 0 1 8 4.2a3.3 3.3 0 0 1 6.5 1.4C14.5 10 8 14 8 14z"/></svg></span></div><div class="meta"><div><h3>Japan digital art</h3><p>by: LumaDesk</p></div><div class="spec">5.4Mb<br>3480x2300</div></div></article>
        <article class="card"><div class="thumb art-sunset" role="img" aria-label="Figure beneath a tree at fiery sunset"><span class="stars"><b>★★★</b>★★</span><span class="fav"><svg viewBox="0 0 16 16"><path d="M8 14S1.5 10 1.5 5.6A3.3 3.3 0 0 1 8 4.2a3.3 3.3 0 0 1 6.5 1.4C14.5 10 8 14 8 14z"/></svg></span></div><div class="meta"><div><h3>Japan digital art</h3><p>by: LumaDesk</p></div><div class="spec">5.4Mb<br>3480x2300</div></div></article>
        <article class="card"><div class="thumb art-moon" role="img" aria-label="Wanderer under a large blue moon"><span class="stars"><b>★★★★</b>★</span><span class="fav"><svg viewBox="0 0 16 16"><path d="M8 14S1.5 10 1.5 5.6A3.3 3.3 0 0 1 8 4.2a3.3 3.3 0 0 1 6.5 1.4C14.5 10 8 14 8 14z"/></svg></span></div><div class="meta"><div><h3>Japan digital art</h3><p>by: LumaDesk</p></div><div class="spec">5.4Mb<br>3480x2300</div></div></article>
        <article class="card"><div class="thumb art-storm" role="img" aria-label="Warrior in a misty grass field"><span class="stars"><b>★★★</b>★★</span><span class="fav"><svg viewBox="0 0 16 16"><path d="M8 14S1.5 10 1.5 5.6A3.3 3.3 0 0 1 8 4.2a3.3 3.3 0 0 1 6.5 1.4C14.5 10 8 14 8 14z"/></svg></span></div><div class="meta"><div><h3>Japan digital art</h3><p>by: LumaDesk</p></div><div class="spec">5.4Mb<br>3480x2300</div></div></article>
        <article class="card"><div class="thumb art-cliff" role="img" aria-label="Caped hero before burning cliffs"><span class="stars"><b>★★★</b>★★</span><span class="fav"><svg viewBox="0 0 16 16"><path d="M8 14S1.5 10 1.5 5.6A3.3 3.3 0 0 1 8 4.2a3.3 3.3 0 0 1 6.5 1.4C14.5 10 8 14 8 14z"/></svg></span></div><div class="meta"><div><h3>Japan digital art</h3><p>by: LumaDesk</p></div><div class="spec">5.4Mb<br>3480x2300</div></div></article>
        <article class="card"><div class="thumb art-blaze" role="img" aria-label="Figure standing in an orange explosion"><span class="stars"><b>★★★</b>★★</span><span class="fav"><svg viewBox="0 0 16 16"><path d="M8 14S1.5 10 1.5 5.6A3.3 3.3 0 0 1 8 4.2a3.3 3.3 0 0 1 6.5 1.4C14.5 10 8 14 8 14z"/></svg></span></div><div class="meta"><div><h3>Japan digital art</h3><p>by: LumaDesk</p></div><div class="spec">5.4Mb<br>3480x2300</div></div></article>
        <article class="card"><div class="thumb art-stars" role="img" aria-label="Girl under a starry orange sky"><span class="stars"><b>★★★</b>★★</span><span class="fav"><svg viewBox="0 0 16 16"><path d="M8 14S1.5 10 1.5 5.6A3.3 3.3 0 0 1 8 4.2a3.3 3.3 0 0 1 6.5 1.4C14.5 10 8 14 8 14z"/></svg></span></div></article>
        <article class="card"><div class="thumb art-temple" role="img" aria-label="Duel before a misty temple"><span class="stars"><b>★★★★</b>★</span><span class="fav"><svg viewBox="0 0 16 16"><path d="M8 14S1.5 10 1.5 5.6A3.3 3.3 0 0 1 8 4.2a3.3 3.3 0 0 1 6.5 1.4C14.5 10 8 14 8 14z"/></svg></span></div></article>
        <article class="card"><div class="thumb art-neon" role="img" aria-label="Neon red and blue abstract creatures"><span class="stars"><b>★★★★</b>★</span><span class="fav"><svg viewBox="0 0 16 16"><path d="M8 14S1.5 10 1.5 5.6A3.3 3.3 0 0 1 8 4.2a3.3 3.3 0 0 1 6.5 1.4C14.5 10 8 14 8 14z"/></svg></span></div></article>
      </div>
      <div class="scrollbar"></div>
    </main>
  </section>

  <!-- DARK SCHEME -->
  <section class="window dark">
    <header class="titlebar">
      <div class="app-name"><span class="mark"></span>LumaDesk</div>
      <div class="win-controls">
        <svg class="ico" viewBox="0 0 16 16"><path d="M3 8h10"/></svg>
        <svg class="ico" viewBox="0 0 16 16"><rect x="2.5" y="5" width="8.5" height="8.5"/><path d="M5 5V2.5h8.5V11H11"/></svg>
        <svg class="ico" viewBox="0 0 16 16"><path d="M3 3l10 10M13 3L3 13"/></svg>
      </div>
    </header>
    <aside class="sidebar">
      <nav class="tabs">
        <div class="tab"><svg class="ico" viewBox="0 0 16 16"><rect x="2" y="2" width="12" height="12"/><path d="M4 12l3-3 2 2 3-3"/></svg>Wallpapers</div>
        <span class="sep"></span>
        <div class="tab off"><svg class="ico" viewBox="0 0 16 16"><rect x="1.5" y="3" width="13" height="8.5"/><path d="M6 14h4"/></svg>ScreenSavers</div>
      </nav>
      <div class="monitor current"><div class="laptop"><div class="screen art-tree" role="img" aria-label="Tree at dusk wallpaper on first display"></div><div class="base"></div></div></div>
      <div class="monitor second"><div class="laptop"><div class="screen art-night" role="img" aria-label="Moonlit scene wallpaper on second display"></div><div class="base"></div></div></div>
      <p class="info-line" style="top:201px"><span>Display 1:</span>Norvia G13L</p>
      <p class="info-line" style="top:227px"><span>Wallpaper:</span> System Default</p>
      <div class="row-buttons" style="top:263px">
        <div class="btn"><svg class="ico" viewBox="0 0 16 16"><circle cx="8" cy="8" r="2.2"/><path d="M8 1.5v2M8 12.5v2M1.5 8h2M12.5 8h2M3.4 3.4l1.4 1.4M11.2 11.2l1.4 1.4M3.4 12.6l1.4-1.4M11.2 4.8l1.4-1.4"/></svg>Settings</div>
        <div class="btn"><svg class="ico" viewBox="0 0 16 16"><rect x="1.5" y="2.5" width="13" height="9"/><path d="M6 14h4M9 7h4"/></svg>Next</div>
        <div class="btn"><svg class="ico" viewBox="0 0 16 16"><rect x="1.5" y="3.5" width="13" height="9"/><path d="M1.5 6h13"/></svg>View</div>
        <div class="dots"><i></i></div>
      </div>
      <div class="divider" style="top:328px"></div>
      <div class="preview thumb art-lake" role="img" aria-label="Pagoda on a lake at pink sunset">
        <span class="stars"><b>★★★★</b>★</span>
        <span class="fav"><svg viewBox="0 0 16 16"><path d="M8 14S1.5 10 1.5 5.6A3.3 3.3 0 0 1 8 4.2a3.3 3.3 0 0 1 6.5 1.4C14.5 10 8 14 8 14z"/></svg></span>
      </div>
      <h2 class="preview-title">Japan digital art</h2>
      <p class="preview-by">by: LumaDesk</p>
      <p class="preview-spec"><span>Image Size:</span>5.4Mb<br><span>Resolution:</span>3480x2300</p>
      <div class="row-buttons" style="top:626px">
        <div class="btn"><svg class="ico" viewBox="0 0 16 16"><path d="M3 8.5l3 3 7-7"/></svg>Apply</div>
        <div class="btn"><svg class="ico" viewBox="0 0 16 16"><rect x="2" y="3" width="12" height="10"/><path d="M2 6.5h12M2 9.5h12"/></svg>Try</div>
        <div class="btn"><svg class="ico" viewBox="0 0 16 16"><rect x="2" y="2" width="12" height="12"/><path d="M5 8h6"/></svg>Uninstall</div>
        <div class="dots"><i></i></div>
      </div>
      <div class="divider" style="top:682px"></div>
      <div class="cta"><svg class="ico" viewBox="0 0 16 16"><path d="M9 2H2v12h12V7M11 1v5M8.5 3.5h5"/></svg>Create your own Wallpaper</div>
    </aside>
    <main class="content">
      <div class="source">
        <div class="item off"><svg class="ico" viewBox="0 0 16 16"><rect x="2" y="2" width="12" height="12"/><path d="M8 4.5v6M5.5 8l2.5 2.5L10.5 8"/></svg>Installed</div>
        <div class="item on"><svg class="ico" viewBox="0 0 16 16"><rect x="1.5" y="2.5" width="13" height="9"/><path d="M6 14h4"/></svg>Workshop</div>
      </div>
      <div class="scheme">
        <div class="item"><svg class="ico" viewBox="0 0 16 16"><circle cx="8" cy="8" r="3"/><path d="M8 1v1.8M8 13.2V15M1 8h1.8M13.2 8H15M3 3l1.3 1.3M11.7 11.7L13 13M3 13l1.3-1.3M11.7 4.3L13 3"/></svg>Light</div>
        <div class="item on moon"><svg class="ico" viewBox="0 0 16 16" style="fill:currentColor;stroke:none"><path d="M9.5 1.5a6.5 6.5 0 1 0 5 9.5A5.5 5.5 0 0 1 9.5 1.5z"/></svg>Dark</div>
      </div>
      <div class="filters">
        <div class="field search"><svg class="ico" viewBox="0 0 16 16"><circle cx="7" cy="7" r="5"/><path d="M11 11l3.5 3.5"/></svg>Search for Wallpapers</div>
        <div class="field creator"><svg class="ico" viewBox="0 0 16 16"><circle cx="8" cy="5" r="3"/><path d="M2.5 14.5c0-3 2.5-4.5 5.5-4.5s5.5 1.5 5.5 4.5z"/></svg>Creator</div>
        <div class="field category"><svg class="ico" viewBox="0 0 16 16"><rect x="2" y="2" width="4.5" height="4.5"/><rect x="9.5" y="2" width="4.5" height="4.5"/><rect x="2" y="9.5" width="4.5" height="4.5"/><rect x="9.5" y="9.5" width="4.5" height="4.5"/></svg>Category</div>
        <div class="field rating"><svg class="ico" viewBox="0 0 16 16"><path d="M8 1.8l1.9 3.9 4.3.6-3.1 3 .7 4.3L8 11.6l-3.8 2 .7-4.3-3.1-3 4.3-.6z"/></svg>Rating</div>
        <div class="round"><i></i></div>
      </div>
      <div class="gallery">
        <article class="card"><div class="thumb art-lake" role="img" aria-label="Pagoda on a lake at pink sunset"><span class="stars"><b>★★★★</b>★</span><span class="fav"><svg viewBox="0 0 16 16"><path d="M8 14S1.5 10 1.5 5.6A3.3 3.3 0 0 1 8 4.2a3.3 3.3 0 0 1 6.5 1.4C14.5 10 8 14 8 14z"/></svg></span></div><div class="meta"><div><h3>Japan digital art</h3><p>by: LumaDesk</p></div><div class="spec">5.4Mb<br>3480x2300</div></div></article>
        <article class="card"><div class="thumb art-sunset" role="img" aria-label="Figure beneath a tree at fiery sunset"><span class="stars"><b>★★★</b>★★</span><span class="fav"><svg viewBox="0 0 16 16"><path d="M8 14S1.5 10 1.5 5.6A3.3 3.3 0 0 1 8 4.2a3.3 3.3 0 0 1 6.5 1.4C14.5 10 8 14 8 14z"/></svg></span></div><div class="meta"><div><h3>Japan digital art</h3><p>by: LumaDesk</p></div><div class="spec">5.4Mb<br>3480x2300</div></div></article>
        <article class="card"><div class="thumb art-moon" role="img" aria-label="Wanderer under a large blue moon"><span class="stars"><b>★★★★</b>★</span><span class="fav"><svg viewBox="0 0 16 16"><path d="M8 14S1.5 10 1.5 5.6A3.3 3.3 0 0 1 8 4.2a3.3 3.3 0 0 1 6.5 1.4C14.5 10 8 14 8 14z"/></svg></span></div><div class="meta"><div><h3>Japan digital art</h3><p>by: LumaDesk</p></div><div class="spec">5.4Mb<br>3480x2300</div></div></article>
        <article class="card"><div class="thumb art-storm" role="img" aria-label="Warrior in a misty grass field"><span class="stars"><b>★★★</b>★★</span><span class="fav"><svg viewBox="0 0 16 16"><path d="M8 14S1.5 10 1.5 5.6A3.3 3.3 0 0 1 8 4.2a3.3 3.3 0 0 1 6.5 1.4C14.5 10 8 14 8 14z"/></svg></span></div><div class="meta"><div><h3>Japan digital art</h3><p>by: LumaDesk</p></div><div class="spec">5.4Mb<br>3480x2300</div></div></article>
        <article class="card"><div class="thumb art-cliff" role="img" aria-label="Caped hero before burning cliffs"><span class="stars"><b>★★★</b>★★</span><span class="fav"><svg viewBox="0 0 16 16"><path d="M8 14S1.5 10 1.5 5.6A3.3 3.3 0 0 1 8 4.2a3.3 3.3 0 0 1 6.5 1.4C14.5 10 8 14 8 14z"/></svg></span></div><div class="meta"><div><h3>Japan digital art</h3><p>by: LumaDesk</p></div><div class="spec">5.4Mb<br>3480x2300</div></div></article>
        <article class="card"><div class="thumb art-blaze" role="img" aria-label="Figure standing in an orange explosion"><span class="stars"><b>★★★</b>★★</span><span class="fav"><svg viewBox="0 0 16 16"><path d="M8 14S1.5 10 1.5 5.6A3.3 3.3 0 0 1 8 4.2a3.3 3.3 0 0 1 6.5 1.4C14.5 10 8 14 8 14z"/></svg></span></div><div class="meta"><div><h3>Japan digital art</h3><p>by: LumaDesk</p></div><div class="spec">5.4Mb<br>3480x2300</div></div></article>
        <article class="card"><div class="thumb art-stars" role="img" aria-label="Girl under a starry orange sky"><span class="stars"><b>★★★</b>★★</span><span class="fav"><svg viewBox="0 0 16 16"><path d="M8 14S1.5 10 1.5 5.6A3.3 3.3 0 0 1 8 4.2a3.3 3.3 0 0 1 6.5 1.4C14.5 10 8 14 8 14z"/></svg></span></div></article>
        <article class="card"><div class="thumb art-temple" role="img" aria-label="Duel before a misty temple"><span class="stars"><b>★★★★</b>★</span><span class="fav"><svg viewBox="0 0 16 16"><path d="M8 14S1.5 10 1.5 5.6A3.3 3.3 0 0 1 8 4.2a3.3 3.3 0 0 1 6.5 1.4C14.5 10 8 14 8 14z"/></svg></span></div></article>
        <article class="card"><div class="thumb art-neon" role="img" aria-label="Neon red and blue abstract creatures"><span class="stars"><b>★★★★</b>★</span><span class="fav"><svg viewBox="0 0 16 16"><path d="M8 14S1.5 10 1.5 5.6A3.3 3.3 0 0 1 8 4.2a3.3 3.3 0 0 1 6.5 1.4C14.5 10 8 14 8 14z"/></svg></span></div></article>
      </div>
      <div class="scrollbar"></div>
    </main>
  </section>
</div>
</body>
</html>
```